Stellan App | Pre-Launch Homepage

Dear designer,
Stellan is a soon to be launched innovative & free social platform for collaborative addictions quitting.
We require a design for our pre-launch homepage that will elevate our basic wireframes to the next level.
We would like the wireframes to serve as a guideline only, and not as a final version of the design. If you have cool ideas - we would appreciate your creativity!
* This is a pre-launch website for a mobile app, and as such the design must be consistent with the general style, design and atmosphere of the app (see screenshot in the shared Drive link).
* We liked the style and feel of the following website: http://plumvane.com/ - Please let's use it as a reference as well.
* The existing text in the wireframes is there just to represent a place for text. Copy will be edited by us after the design is done.
Please find the wireframes attached, and all relevant design assets and app screenshots in the following Drive shared link -
https://files.orbelink.com/open?id=7K204XqR3tPmHc8Lw2Jd61VnaGzT
Thanks,
Marcus
Industry/Entity Type
Social
Number of Pages Required
1 page
Look and feel
Each slider illustrates characteristics of the customer's brand and the style your logo design should communicate.

```html
<!DOCTYPE html>
<html lang="en">
<head>
<meta charset="utf-8">
<title>Stellan App | Pre-Launch Homepage</title>
<link href="https://fonts.googleapis.com/css2?family=Lato:wght@300;400;700;900&family=Open+Sans:wght@400;600;700&display=swap" rel="stylesheet">
<style>
:root{
  --hero-a:#3b2b24;
  --hero-b:#26303d;
  --hero-c:#1b222e;
  --lime:#d9e24b;
  --red:#f0545a;
  --green:#2ecc9a;
  --achieve:#3dbf79;
  --orange:#f4a43a;
  --blue:#4aa9e0;
  --sky:#7dd3ec;
  --light:#f3f3f3;
  --ink:#3a3a3a;
  --muted:#8a8a8a;
  --slate:#4b4f5f;
  --slate-dark:#434756;
  --white:#ffffff;
}
*{box-sizing:border-box;margin:0;padding:0}
html,body{width:1200px;height:3300px;overflow:hidden}
body{font-family:"Open Sans",sans-serif;color:var(--ink);background:var(--white)}
section{position:relative;width:1200px;overflow:visible}
.art{position:absolute;border-radius:12px}

/* hero */
.hero{height:600px;background:radial-gradient(circle at 25% 40%,#4a3a2e 0,transparent 45%),linear-gradient(135deg,var(--hero-a),var(--hero-b) 55%,var(--hero-c))}
.brand{position:absolute;left:40px;top:26px;color:var(--white)}
.brand-name{font-family:"Lato",sans-serif;font-weight:700;font-size:46px;line-height:1}
.brand-tag{font-size:15px;margin-top:8px;opacity:.9}
.contact-btn{position:absolute;left:900px;top:44px;background:var(--green);color:var(--white);font-size:13px;font-weight:700;letter-spacing:.5px;padding:10px 18px;border-radius:4px;text-transform:uppercase;display:flex;align-items:center;gap:8px}
.headline{position:absolute;left:160px;top:268px;width:560px;font-family:"Lato",sans-serif;font-size:40px;line-height:1.18;color:var(--lime);font-weight:400}
.subscribe-note{position:absolute;left:160px;top:470px;color:var(--white);font-size:16px}
.signup{position:absolute;display:flex}
.signup .field{width:300px;height:40px;background:var(--white);border-radius:3px 0 0 3px;font-size:13px;color:#999;padding:11px 14px}
.signup .btn{height:40px;background:var(--red);color:var(--white);font-size:13px;font-weight:700;padding:11px 16px;border-radius:0 3px 3px 0;text-transform:uppercase}
.hero .signup{left:160px;top:510px}
.hero-phone{left:720px;top:120px;width:190px;height:420px;border-radius:34px;background:linear-gradient(160deg,#f36f6a,#d4464d);transform:rotate(-6deg)}
.scroll-dot{position:absolute;left:582px;width:36px;height:36px;border-radius:50%;display:flex;align-items:center;justify-content:center;z-index:2}

/* features */
.features{height:400px;background:var(--light)}
.feature-row{position:absolute;top:120px;left:150px;width:900px;display:flex;justify-content:space-between}
.feature{width:260px;text-align:center}
.feature-icon{width:70px;height:70px;border-radius:50%;margin:0 auto 24px;display:flex;align-items:center;justify-content:center}
.feature h3{font-family:"Lato",sans-serif;font-weight:900;font-size:20px;letter-spacing:.5px;color:var(--ink);text-transform:uppercase}
.feature p{font-size:13px;color:var(--muted);margin-top:8px;line-height:1.5}

/* content blocks */
.block-title{font-family:"Lato",sans-serif;font-weight:700;font-size:38px}
.block-copy{font-size:13px;line-height:1.65;color:var(--muted);margin-top:14px}
.fun{height:440px}
.fun-art{left:120px;top:40px;width:400px;height:360px;border-radius:50%;background:radial-gradient(circle,#f6f8f0 0 35%,#d9eec4 55%,#f6d9c4 75%,transparent 76%)}
.fun-text{position:absolute;left:660px;top:110px;width:360px}
.fun-text .block-title{color:var(--red);text-align:center}

.inspire{height:480px;background:var(--sky)}
.inspire-text{position:absolute;left:170px;top:140px;width:360px;text-align:center}
.inspire-text .block-title{color:#2f5f72}
.inspire-text .block-copy{color:#2f6b80}
.inspire-art{left:620px;top:40px;width:460px;height:400px;border-radius:50%;background:radial-gradient(circle at 40% 50%,#bfeaf6 0,#9cdff1 45%,transparent 70%)}

.achieve{height:480px}
.achieve-head{position:absolute;left:350px;top:40px;width:500px;text-align:center}
.achieve-head .block-title{color:var(--achieve)}
.achieve-art{left:470px;top:190px;width:260px;height:290px;border-radius:130px 130px 0 0;background:linear-gradient(180deg,#f6e7c8,#e9c98f)}
.goal{position:absolute;display:flex;align-items:center;gap:18px;width:340px}
.goal p{font-size:13px;color:var(--ink);line-height:1.45}
.goal-icon{flex:none;width:64px;height:64px;border-radius:50%;display:flex;align-items:center;justify-content:center}
.goal.right{flex-direction:row-reverse;text-align:left}

/* coming soon */
.coming{height:900px;background:var(--slate);color:var(--white);text-align:center}
.coming h2{position:absolute;left:0;top:66px;width:1200px;font-family:"Lato",sans-serif;font-weight:700;font-size:36px}
.coming-phone{left:520px;top:140px;width:160px;height:330px;border-radius:26px;background:linear-gradient(180deg,#f7f7f7,#e6e6e6)}
.stores{position:absolute;left:510px;top:500px;display:flex;gap:30px}
.stores span{width:40px;height:40px;border-radius:50%;background:var(--white);opacity:.9}
.coming .subscribe-note{left:0;top:584px;width:1200px;font-weight:700;font-size:17px}
.coming .signup{left:430px;top:624px}
.join{position:absolute;left:0;top:710px;width:1200px;font-weight:700;font-size:18px}
.socials{position:absolute;left:540px;top:752px;display:flex;gap:16px}
.socials span{width:36px;height:36px;border-radius:50%}
.legal{position:absolute;left:0;top:820px;width:1200px;font-size:11px;color:#b9bccb}
.footer-links{position:absolute;left:0;top:850px;width:1200px;font-size:11px;color:#b9bccb}
</style>
</head>
<body>

<section class="hero">
  <div class="brand">
    <div class="brand-name">Stellan</div>
    <div class="brand-tag">Become a Better Version of Yourself</div>
  </div>
  <div class="contact-btn">
    <svg width="14" height="14" viewBox="0 0 24 24"><path fill="#fff" d="M6.6 10.8a15 15 0 0 0 6.6 6.6l2.2-2.2a1 1 0 0 1 1-.25 11.4 11.4 0 0 0 3.6.57 1 1 0 0 1 1 1V20a1 1 0 0 1-1 1A17 17 0 0 1 3 4a1 1 0 0 1 1-1h3.5a1 1 0 0 1 1 1c0 1.25.2 2.45.57 3.6a1 1 0 0 1-.25 1z"/></svg>
    Contact us
  </div>
  <h1 class="headline">Stellan is a revolutionary &amp; free social platform for collaborative addictions quitting.</h1>
  <p class="subscribe-note">Subscribe below for the beta release and updates.</p>
  <div class="signup"><div class="field">Enter your email address</div><div class="btn">Let me know!</div></div>
  <div class="art hero-phone" role="img" aria-label="Red smartphone showing the app's profile screen"></div>
</section>

<div class="scroll-dot" style="top:582px;background:var(--white)">
  <svg width="14" height="14" viewBox="0 0 24 24"><rect x="8" y="4" width="8" height="14" rx="4" fill="none" stroke="#555" stroke-width="2"/></svg>
</div>

<section class="features">
  <div class="feature-row">
    <div class="feature">
      <div class="feature-icon" style="background:var(--red)">
        <svg width="30" height="30" viewBox="0 0 24 24"><text x="12" y="19" text-anchor="middle" font-family="Lato,sans-serif" font-weight="900" font-size="20" fill="#fff">?</text></svg>
      </div>
      <h3>Never be alone</h3>
      <p>Forget what you know - Stellan<br>makes it fun to quit.</p>
    </div>
    <div class="feature">
      <div class="feature-icon" style="background:var(--orange)">
        <svg width="30" height="30" viewBox="0 0 24 24"><path fill="#fff" d="M12 2l3 6.5 7 .8-5.2 4.8 1.5 7L12 17.6 5.7 21.1l1.5-7L2 9.3l7-.8z"/></svg>
      </div>
      <h3>Network power</h3>
      <p>Forget what you know - Stellan<br>makes it fun to quit.</p>
    </div>
    <div class="feature">
      <div class="feature-icon" style="background:var(--blue)">
        <svg width="30" height="30" viewBox="0 0 24 24"><path fill="none" stroke="#fff" stroke-width="3" d="M5 12l5 5 9-10"/></svg>
      </div>
      <h3>Stay motivated</h3>
      <p>Forget what you know - Stellan<br>makes it fun to quit.</p>
    </div>
  </div>
</section>

<div class="scroll-dot" style="top:982px">
  <svg width="14" height="14" viewBox="0 0 24 24"><path d="M6 9l6 6 6-6" fill="none" stroke="#555" stroke-width="2.5"/></svg>
</div>

<section class="fun">
  <div class="art fun-art" role="img" aria-label="Illustration of a green phone encircled by colourful social app icons"></div>
  <div class="fun-text">
    <h2 class="block-title">Fun</h2>
    <p class="block-copy">Forget what you know - Stellan makes it fun to quit. The battle between your mind and bad habits turns into a fresh, gamified journey for managing your cravings.</p>
    <p class="block-copy">Stellan gives you the chance to take an active role in helping your network to reach their goals as a team. That's right, we turned the quitting process into a social game.</p>
  </div>
</section>

<section class="inspire">
  <div class="inspire-text">
    <h2 class="block-title">Inspire</h2>
    <p class="block-copy">One of the most important factors for successful quitting is the ability to stay inspired during the process.</p>
    <p class="block-copy">That's why we designed Stellan as a platform where you can inspire and be inspired by a supportive network of people quitting alongside you.</p>
  </div>
  <div class="art inspire-art" role="img" aria-label="Illustration of a blue phone linked to a network of friend avatars"></div>
</section>

<section class="achieve">
  <div class="achieve-head">
    <h2 class="block-title">Achieve</h2>
    <p class="block-copy">Stellan is built as a pyramid of relationships that make use of the Social Cognitive Theory, to provide a powerful network of supportive achievements.</p>
    <p class="block-copy" style="margin-top:6px">The bigger your crew, the stronger you get.</p>
  </div>
  <div class="art achieve-art" role="img" aria-label="Illustration of a hand holding a phone showing achievements"></div>

  <div class="goal" style="left:140px;top:250px">
    <div class="goal-icon" style="background:#fbe9c4"><svg width="30" height="30" viewBox="0 0 24 24"><path fill="#e8a52c" d="M7 3h10v5a5 5 0 0 1-10 0zM11 13h2v4h3v3H8v-3h3z"/></svg></div>
    <p>Stellan is built as a pyramid of relationships that makes use of the Social Cognitive Theory</p>
  </div>
  <div class="goal" style="left:140px;top:350px">
    <div class="goal-icon" style="background:#fbd9d9"><svg width="30" height="30" viewBox="0 0 24 24"><path fill="#e2524f" d="M3 9h18l-2 11H5zM8 9l4-5 4 5"/></svg></div>
    <p>Stellan is built as a pyramid of relationships that makes use of the Social Cognitive Theory</p>
  </div>
  <div class="goal right" style="left:720px;top:250px">
    <div class="goal-icon" style="background:#fbe9c4"><svg width="30" height="30" viewBox="0 0 24 24"><path fill="#e8a52c" d="M7 3h10v5a5 5 0 0 1-10 0zM11 13h2v4h3v3H8v-3h3z"/></svg></div>
    <p>Stellan is built as a pyramid of relationships that makes use of the Social Cognitive Theory</p>
  </div>
  <div class="goal right" style="left:720px;top:350px">
    <div class="goal-icon" style="background:#fbd9d9"><svg width="30" height="30" viewBox="0 0 24 24"><path fill="#e2524f" d="M3 9h18l-2 11H5zM8 9l4-5 4 5"/></svg></div>
    <p>Stellan is built as a pyramid of relationships that makes use of the Social Cognitive Theory</p>
  </div>
</section>

<section class="coming">
  <h2>Coming Soon</h2>
  <div class="art coming-phone" role="img" aria-label="White smartphone showing the app's home screen"></div>
  <div class="stores"><span></span><span></span><span></span></div>
  <p class="subscribe-note">Subscribe below for the beta release and updates.</p>
  <div class="signup"><div class="field">Enter your email address</div><div class="btn">Let me know!</div></div>
  <p class="join">Join the revolution</p>
  <div class="socials">
    <span style="background:#3b5b98"></span>
    <span style="background:#8d93a6"></span>
    <span style="background:#3fa7e0"></span>
  </div>
  <p class="legal">Copyright © 2015 Stellan.com</p>
  <p class="footer-links">Contact Us &nbsp;|&nbsp; FAQ &nbsp;|&nbsp; Privacy Policy</p>
</section>

</body>
</html>
```